Irrigation Business needs their business cards modernised and revamped

I would like to keep my current logo, colours and revamp the format of the card.

I would like the card to be clean yet important.

Im not sure if you include texture but i would like the named logo to be indented into the card etc.

show me something alive and free something thats clinical to the point yet has a feel of achievement. i would like people to go nice card.

Target Market(s)

high end clients, corporate, sports field manger, the guys that make the decisions

Industry/Entity Type

Business

Contact Information for Business Card

nformation to be included

Dorian Hesk (Director)
0487253916
dorian@tfcraft.biz
www.taddsfieldcrafts.com

instagram logo
google logo
facebook logo

Colors

Designer to choose colors to be used in the design.

Requirements
Nice to have
• indentations a really nice feel to the card good texture

```html
<!DOCTYPE html>
<html lang="en">
<head>
<meta charset="utf-8">
<title>Tadd's Field Crafts — Business Card</title>
<link rel="stylesheet" href="https://fonts.googleapis.com/css2?family=Montserrat:wght@800&family=Oswald:wght@500&family=Open+Sans:wght@400&display=swap">
<style>
  :root {
    --backdrop: #1d1d1f;
    --card: #f4f5f6;
    --brand-blue: #2660ac;
    --sky-blue: #3a9fd4;
    --field-green: #2a9a48;
    --ink: #2b2b2b;
    --rule: #3a3a3a;
  }
  * { margin: 0; padding: 0; box-sizing: border-box; }
  html, body { width: 1200px; height: 904px; overflow: hidden; }
  body { background: var(--backdrop); position: relative; }

  .card {
    position: absolute;
    width: 560px;
    height: 320px;
    background: linear-gradient(160deg, #ffffff 0%, var(--card) 100%);
    box-shadow: 0 18px 40px rgba(0,0,0,.55);
    overflow: hidden;
  }
  .card--front { left: 80px; top: 110px; }
  .card--back  { left: 560px; top: 474px; }

  /* Front */
  .brand {
    position: absolute; inset: 0;
    display: flex; flex-direction: column; align-items: center; justify-content: center;
    gap: 16px;
  }
  .brand__dot {
    width: 74px; height: 74px; border-radius: 50%;
    background: var(--brand-blue);
  }
  .brand__name {
    font-family: 'Montserrat', sans-serif;
    font-weight: 800;
    font-size: 30px;
    letter-spacing: .5px;
    color: var(--brand-blue);
    text-transform: uppercase;
  }

  /* Back */
  .identity {
    position: absolute; right: 274px; top: 100px;
    text-align: right;
  }
  .identity__name {
    font-family: 'Oswald', sans-serif;
    font-weight: 500;
    font-size: 38px;
    line-height: 1;
    color: var(--brand-blue);
    text-transform: uppercase;
    letter-spacing: -.5px;
    white-space: nowrap;
  }
  .identity__role {
    font-family: 'Open Sans', sans-serif;
    font-size: 14px;
    color: var(--field-green);
    margin-top: 2px;
  }
  .divider {
    position: absolute; left: 298px; top: 92px;
    width: 1.5px; height: 76px; background: var(--rule);
  }
  .contacts {
    position: absolute; left: 314px; top: 92px;
    list-style: none;
    font-family: 'Open Sans', sans-serif;
    font-size: 14px;
    color: var(--ink);
  }
  .contacts li { display: flex; align-items: center; gap: 8px; height: 24px; white-space: nowrap; }
  .contacts svg { width: 13px; height: 13px; flex: none; }

  .social {
    position: absolute; left: 262px; top: 232px;
    display: flex; gap: 10px;
  }
  .social__tile {
    width: 26px; height: 26px; border-radius: 4px;
    background: var(--brand-blue);
  }
</style>
</head>
<body>

<section class="card card--front">
  <div class="brand">
    <div class="brand__dot"></div>
    <div class="brand__name">Tadd's Field Crafts</div>
  </div>
</section>

<section class="card card--back">
  <div class="identity">
    <div class="identity__name">Dorian Hesk</div>
    <div class="identity__role">Director</div>
  </div>

  <div class="divider"></div>

  <ul class="contacts">
    <li>
      <svg viewBox="0 0 16 16" aria-hidden="true"><path d="M4 1.5l2.5 3-1.4 1.6c.9 1.9 2.4 3.4 4.3 4.3l1.6-1.4 3 2.5-1.5 2.2C7 13.5 2.5 9 1.8 3z" fill="var(--sky-blue)"/></svg>
      0487253916
    </li>
    <li>
      <svg viewBox="0 0 16 16" aria-hidden="true"><rect x="1" y="3.5" width="14" height="9" rx="1" fill="var(--sky-blue)"/><path d="M1.5 4l6.5 5 6.5-5" stroke="#fff" stroke-width="1.3" fill="none"/></svg>
      dorian@tfcraft.biz
    </li>
    <li>
      <svg viewBox="0 0 16 16" aria-hidden="true"><circle cx="8" cy="8" r="6.5" fill="none" stroke="var(--sky-blue)" stroke-width="1.5"/><ellipse cx="8" cy="8" rx="2.8" ry="6.5" fill="none" stroke="var(--sky-blue)" stroke-width="1.2"/><path d="M1.5 8h13" stroke="var(--sky-blue)" stroke-width="1.2"/></svg>
      www.taddsfieldcrafts.com
    </li>
  </ul>

  <div class="social" aria-label="Social profiles">
    <span class="social__tile"></span>
    <span class="social__tile"></span>
    <span class="social__tile"></span>
  </div>
</section>

</body>
</html>
```